Buch-/eBook-Cover für einen Elternratgeber
Zielgruppe
Buch: Elternratgeber
Titel: Zahlen fühlen
Untertitel: Deinem Kind den richtigen Umgang beibringen
Wir sind der ULM Verlag und suchen ein passendes Cover für unseren neuen Elternratgeber. Mit diesem Buch möchten wir Eltern unterstützen, ihren Kindern einen guten und verantwortungsvollen Umgang mit Geld zu vermitteln.
Anforderungen an das Cover-Design:
Bitte keinen Comicstil
Das Buch richtet sich an Eltern (nicht kindlich oder verspielt gestalten)
Keine direkte Darstellung von Geld (z. B. keine Münzen, Geldscheine, Sparschweine usw.)
Ob mit oder ohne Personen auf dem Cover: sind wir offen
Farbwahl und Bildsprache: gerne seriös, ansprechend und modern
Wir sind gespannt auf kreative und professionelle Vorschläge!
E-Book E-Book"
Das Design darf nicht zu überladen sein.

```html
<!DOCTYPE html>
<html lang="de">
<head>
<meta charset="utf-8">
<title>Zahlen fühlen – Buchcover</title>
<link rel="stylesheet" href="https://fonts.googleapis.com/css2?family=Source+Serif+4:opsz,wght@8..60,400;8..60,500;8..60,600&display=swap">
<style>
  :root {
    --backdrop-sand: #eaddcc;
    --wave-mist: #aab5b9;
    --wave-slate: #7e96a1;
    --wave-steel: #4f6f81;
    --wave-navy: #2a4658;
    --cover-cream: #f7f0e4;
    --ink-navy: #1f3346;
    --ink-teal: #2f5266;
    --light-gold: #f1d3a4;
    --light-amber: #d9a46e;
    --field-olive: #8f7a45;
    --path-peach: #e7b894;
    --imprint-cream: #fbf2e6;
  }
  * { margin: 0; padding: 0; box-sizing: border-box; }
  html, body {
    width: 1200px; height: 900px; overflow: hidden;
    background: var(--backdrop-sand);
  }
  .stage { position: relative; width: 1200px; height: 900px; overflow: hidden; }
  .waves { position: absolute; inset: 0; width: 1200px; height: 900px; }

  .book-cover {
    position: absolute; left: 326px; top: 0; width: 551px; height: 900px;
    background: var(--cover-cream);
    box-shadow: 6px 0 18px rgba(20, 35, 50, 0.18);
    overflow: hidden;
    font-family: "Source Serif 4", Georgia, serif;
    color: var(--ink-navy);
    text-align: center;
  }
  .author {
    position: absolute; top: 46px; left: 0; right: 0;
    font-size: 22px; font-weight: 400; letter-spacing: 0.06em;
    color: var(--ink-teal);
  }
  .title {
    position: absolute; top: 104px; left: 0; right: 0;
    font-size: 78px; font-weight: 500; line-height: 88px;
    letter-spacing: -0.005em;
  }
  .subtitle {
    position: absolute; top: 276px; left: 0; right: 0;
    font-size: 27px; font-weight: 400; line-height: 40px;
  }
  .cover-photo {
    position: absolute; left: 0; right: 0; top: 380px; bottom: 0;
    background:
      linear-gradient(180deg, var(--cover-cream) 0%, rgba(247,240,228,0) 14%),
      radial-gradient(ellipse 70% 45% at 50% 78%, var(--path-peach) 0%, rgba(231,184,148,0) 70%),
      linear-gradient(180deg, #f3dcb6 0%, var(--light-gold) 22%, #c7b48a 40%, var(--field-olive) 62%, var(--light-amber) 82%, #c48e62 100%);
  }
  .imprint {
    position: absolute; bottom: 36px; left: 0; right: 0;
    font-size: 17px; font-weight: 600; letter-spacing: 0.04em;
    color: var(--imprint-cream);
  }
</style>
</head>
<body>
  <div class="stage">
    <svg class="waves" viewBox="0 0 1200 900" aria-hidden="true">
      <path fill="var(--wave-mist)" d="M0 350 C110 380 230 410 330 395 L330 900 L0 900 Z"/>
      <path fill="var(--wave-slate)" d="M0 560 C120 590 230 610 330 585 L330 900 L0 900 Z"/>
      <path fill="var(--wave-steel)" d="M0 580 C120 600 230 620 330 600 L330 900 L0 900 Z" opacity="0"/>
      <path fill="var(--wave-navy)" d="M0 660 C120 700 240 690 330 665 L330 900 L0 900 Z"/>
      <path fill="var(--wave-mist)" d="M870 265 C980 230 1090 190 1200 205 L1200 900 L870 900 Z"/>
      <path fill="var(--wave-slate)" d="M870 345 C990 320 1100 290 1200 320 L1200 900 L870 900 Z"/>
      <path fill="var(--wave-steel)" d="M870 540 C990 500 1090 480 1200 505 L1200 900 L870 900 Z"/>
      <path fill="var(--wave-navy)" d="M870 660 C990 620 1100 600 1200 615 L1200 900 L870 900 Z"/>
    </svg>

    <article class="book-cover">
      <p class="author">MARA UDENHOF</p>
      <h1 class="title">Zahlen<br>fühlen</h1>
      <p class="subtitle">Deinem Kind den<br>richtigen Umgang beibringen</p>
      <div class="cover-photo" role="img" aria-label="Foto im Gegenlicht: Vater und Kind gehen von hinten gesehen Hand in Hand einen hellen Weg entlang, gesäumt von Gräsern, mit See und Hügeln im goldenen Abendlicht"></div>
      <p class="imprint">ULM VERLAG</p>
    </article>
  </div>
</body>
</html>
```